Dentist Home Page Design

We need a home page design to be used as a responsive wordpress theme for our dentist website. Website overall look and feel should look professional, yet very friendly as going to dentist is not people's favorite thing to do, for most it might even be scary. We want our website to differentiate with its design from all other generic looking cookie cutter dentists and creates a branded feel.
you can use a generic image for the 680x300px banner on the home pageif you like in the meantime). Total width should not exceed 960 px
Please follow the layout on the wireframes, do not add or delete random elements.
Target Market(s)
mostly targets male/female between 30-45, families with kids as well.
Industry/Entity Type
It Professional
Colors
Designer to choose colors to be used in the design.
Look and feel
Each slider illustrates characteristics of the customer's brand and the style your logo design should communicate.

```html
<!DOCTYPE html>
<html lang="en">
<head>
<meta charset="utf-8">
<title>Maplecrest Dental – Home</title>
<link href="https://fonts.googleapis.com/css2?family=Source+Sans+3:wght@400;600;700&display=swap" rel="stylesheet">
<style>
:root{
  --orange:#f7822a;
  --orange-dark:#e86f17;
  --orange-light:#fb9a3f;
  --blue:#1f5bb5;
  --blue-deep:#17499d;
  --link:#2a57a8;
  --ink:#333;
  --white:#fff;
  --thumb:#3a3030;
  --face:#b9a89a;
}
*{box-sizing:border-box;margin:0;padding:0}
html,body{width:1200px;height:900px;overflow:hidden;background:var(--white)}
body{position:relative;font-family:"Source Sans 3",Arial,sans-serif;color:var(--ink)}
.abs{position:absolute}
.video-tile{width:120px}
.video-tile .thumb{background:linear-gradient(160deg,#5b4a48,#241c1c);display:flex;align-items:center;justify-content:center}
.video-tile .label{height:28px;background:var(--orange);color:var(--white);font-size:14px;text-align:center;line-height:29px;border-top:1px solid var(--orange-light)}
.case-tile{width:120px}
.case-tile .thumb{height:55px;background:radial-gradient(ellipse at 50% 90%,#5a5a5a,#111 70%)}
.case-tile .num{height:28px;background:var(--orange-light);color:var(--white);font-size:14px;text-align:center;line-height:28px}
.case-tile .title{height:45px;background:linear-gradient(var(--orange),var(--orange-dark));color:var(--white);font-size:14px;font-weight:700;text-align:center;line-height:44px}
.likes{left:113px;top:237px;font:13px Helvetica,Arial,sans-serif;color:var(--ink);display:flex;align-items:center;gap:5px}
.likes .sq{width:12px;height:12px;background:var(--link);border-radius:2px}
.likes a{color:var(--link);text-decoration:none}
.follow-link{right:128px;top:236px;font-size:14px;color:var(--link);text-decoration:underline}
.fans{left:118px;top:265px;display:flex;gap:3px}
.fans span{width:50px;height:50px;background:linear-gradient(var(--face),#6b5d55)}
.footer{left:0;top:365px;width:1200px;height:518px;background:linear-gradient(180deg,#1b52ab,var(--blue) 60%,#2160ba)}
.footer-base{left:0;top:883px;width:1200px;height:17px;background:var(--blue-deep)}
.footer h2{font-size:21px;font-weight:700;color:var(--white);letter-spacing:-.3px;padding-bottom:5px;border-bottom:1px solid rgba(255,255,255,.2);display:inline-block}
.footer h3{font-size:15px;font-weight:700;color:var(--white);padding-bottom:4px;border-bottom:1px solid rgba(255,255,255,.2);display:inline-block}
.footer p,.footer li{font-size:14.5px;color:var(--white);line-height:18px;list-style:none}
.footer a{color:var(--white);font-size:14.5px;text-decoration:underline;margin-right:16px}
.map{left:417px;top:559px;width:259px;height:231px;background:linear-gradient(135deg,#eceae2 0%,#e6e3d8 55%,#9ec0e6 56%,#8fb4df)}
.field{width:340px;height:36px;background:var(--white);border:1px solid #cfd6e2;font-size:17px;color:#666;padding-left:12px;line-height:35px}
.btn{left:947px;top:671px;width:120px;height:36px;background:var(--orange);color:var(--white);font-size:15px;text-align:center;line-height:36px}
</style>
</head>
<body>

<!-- treatment videos -->
<div class="abs video-tile" style="left:142px;top:0"><div class="thumb" style="height:17px" role="img" aria-label="Dental implants video still"></div><div class="label">Dental Implants</div></div>
<div class="abs video-tile" style="left:295px;top:0"><div class="thumb" style="height:17px" role="img" aria-label="Veneers video still"></div><div class="label">Veneers</div></div>
<div class="abs video-tile" style="left:448px;top:0"><div class="thumb" style="height:17px" role="img" aria-label="Clear aligner video still"></div><div class="label">ClearAlign</div></div>

<div class="abs video-tile" style="left:142px;top:63px"><div class="thumb" style="height:90px" role="img" aria-label="Orthodontics video still"><svg width="40" height="40" viewBox="0 0 40 40"><circle cx="20" cy="20" r="18" fill="rgba(0,0,0,.25)" stroke="#fff" stroke-width="2"/><path d="M16 12l10 8-10 8z" fill="#fff"/></svg></div><div class="label">Orthodontics</div></div>
<div class="abs video-tile" style="left:295px;top:63px"><div class="thumb" style="height:90px" role="img" aria-label="Clip-on smile video still"><svg width="40" height="40" viewBox="0 0 40 40"><circle cx="20" cy="20" r="18" fill="rgba(0,0,0,.25)" stroke="#fff" stroke-width="2"/><path d="M16 12l10 8-10 8z" fill="#fff"/></svg></div><div class="label">Clip-On Smile</div></div>
<div class="abs video-tile" style="left:448px;top:63px"><div class="thumb" style="height:90px" role="img" aria-label="Root canal video still"><svg width="40" height="40" viewBox="0 0 40 40"><circle cx="20" cy="20" r="18" fill="rgba(0,0,0,.25)" stroke="#fff" stroke-width="2"/><path d="M16 12l10 8-10 8z" fill="#fff"/></svg></div><div class="label">Root Canal</div></div>

<!-- case studies -->
<div class="abs case-tile" style="left:637px;top:0"><div class="thumb" role="img" aria-label="Overbite smile result"></div><div class="num">Case Study #1</div><div class="title">Overbite</div></div>
<div class="abs case-tile" style="left:787px;top:0"><div class="thumb" role="img" aria-label="Smile makeover result"></div><div class="num">Case Study #2</div><div class="title">Smile Makeover</div></div>
<div class="abs case-tile" style="left:937px;top:0"><div class="thumb" role="img" aria-label="Dental bridges result"></div><div class="num">Case Study #3</div><div class="title">Dental Bridges</div></div>

<!-- social likes -->
<div class="abs likes"><span class="sq"></span><span><a href="#">Owen Hartley</a>, <a href="#">Ravi Kessler</a> and 2,904,577 others like this.</span></div>
<a class="abs follow-link" href="#">Follow us on PageCircle</a>
<div class="abs fans" role="img" aria-label="Profile pictures of fans">
  <span></span><span></span><span></span><span></span><span></span><span></span><span></span><span></span><span></span><span></span><span></span><span></span><span></span><span></span><span></span><span></span><span></span><span></span>
</div>

<!-- footer -->
<footer class="abs footer">
  <div class="abs" style="left:141px;top:40px;width:230px">
    <h2>Contact Info &amp; Hours</h2>
    <p style="margin-top:20px">Phone: (555) 214-3080<br>Fax: (555) 214-3081</p>
    <p style="margin-top:9px"><a href="#">Email Us</a><a href="#">Request Appointment</a></p>
    <h3 style="margin-top:20px">Maplecrest Dental Office Hours</h3>
    <ul style="margin-top:22px">
      <li>Monday: 12:00 pm-8:00 pm</li>
      <li>Tuesday: 10:00 am-6:00 pm</li>
      <li>Wednesday: 12:00 pm-8:00 pm</li>
      <li>Thursday: 9:00 am-5:00 pm</li>
      <li>Friday: Closed</li>
      <li>Saturday: 10:00 am-3:00 pm</li>
      <li>Sunday/Holidays: Closed</li>
    </ul>
    <h3 style="margin-top:24px">Follow Us</h3>
    <p style="margin-top:18px"><a href="#">Chirper</a><a href="#" style="margin-right:14px">PageCircle</a><a href="#">StreamBox</a></p>
    <p style="margin-top:13px"><a href="#">Take our Survey</a></p>
  </div>

  <div class="abs" style="left:415px;top:40px;width:280px">
    <h2>Address &amp; Directions</h2>
    <p style="margin-top:20px;font-weight:700">Maplecrest Dental</p>
    <p style="margin-top:4px">2417 Harbour Street East,<br>Lakeview, ON K0A 1B2<br><em style="font-size:13px">(Free Parking at the Front)</em></p>
  </div>

  <div class="abs" style="left:726px;top:40px;width:345px">
    <h2>Sign-Up for Our Monthly Newsletter</h2>
    <p style="margin-top:20px;margin-left:-1px">To receive free dental health tips from Dr. Alan Corwin</p>
  </div>
  <div class="abs field" style="left:727px;top:138px">First Name</div>
  <div class="abs field" style="left:727px;top:194px">Best Email</div>
  <div class="abs field" style="left:727px;top:250px">Mobile Phone</div>
  <div class="abs" style="left:727px;top:411px"><a href="#" style="margin-right:14px">Terms of Service</a><a href="#" style="margin-right:14px">Privacy Policy</a><a href="#">Site Map</a></div>
</footer>
<div class="abs map" role="img" aria-label="Street map showing the office location"></div>
<div class="abs btn">Sign Up</div>
<div class="abs footer-base"></div>

</body>
</html>
```